We are starting a new service that will combine local city menus and specials from local restaurants that will then be emailed and printed out on our website.. its a free service to the subscribers and a small charge to the restaurants. We need something to reflect the restaurant industry and to appeal to the general public alike, free to the end user. They sign up and receive daily specials in an email from our site.. not just one city but any one they pick that we service.. We would need links to include. Home, About Us, Sign Up (for free to public), Add Your Restaurant (increase sales and reduce daily calls).. and Contact Us link.. the name of the service is Town Plates in Motion and website will be townplatesinmotion.example. thank you

```html
<!DOCTYPE html>
<html lang="en">
<head>
<meta charset="utf-8">
<title>Town Plates in Motion</title>
<link rel="stylesheet" href="https://fonts.googleapis.com/css2?family=Arimo&family=Lora:wght@700&family=Open+Sans:wght@400&display=swap">
<style>
  :root {
    --page-bg: #ffffff;
    --title-ink: #333333;
    --nav-ink: #555555;
    --nav-active-bg: #f2f2f2;
    --nav-active-ink: #222222;
    --rule: #d6d6d6;
    --hero-white: #ffffff;
    --accent: #f04e3b;
    --icon-grey: #9a9a9a;
    --scene-red: #c8262b;
    --scene-dark: #3b3a2c;
    --scene-light: #e9e6e4;
  }
  * { margin: 0; padding: 0; box-sizing: border-box; }
  html, body {
    width: 1200px;
    height: 672px;
    overflow: hidden;
    background: var(--page-bg);
  }
  .page {
    position: relative;
    width: 1200px;
    height: 672px;
    overflow: hidden;
  }
  .site-title {
    position: absolute;
    top: 4px;
    left: 0;
    width: 100%;
    text-align: center;
    font-family: "Arimo", Arial, sans-serif;
    font-weight: 400;
    font-size: 35px;
    letter-spacing: 0.5px;
    color: var(--title-ink);
  }
  .nav-rule {
    position: absolute;
    top: 88px;
    height: 1px;
    background: var(--rule);
  }
  .nav-rule--left { left: 118px; width: 285px; }
  .nav-rule--right { left: 794px; width: 285px; }
  .main-nav {
    position: absolute;
    top: 71px;
    left: 432px;
    display: flex;
    font-family: "Arimo", Arial, sans-serif;
    font-size: 13px;
    text-transform: uppercase;
  }
  .main-nav a {
    display: block;
    height: 35px;
    line-height: 35px;
    padding: 0 14px;
    color: var(--nav-ink);
    text-decoration: none;
  }
  .main-nav a.is-active {
    background: var(--nav-active-bg);
    color: var(--nav-active-ink);
  }
  .hero {
    position: absolute;
    top: 146px;
    left: 0;
    width: 1200px;
    height: 482px;
    overflow: hidden;
  }
  .hero-backdrop {
    position: absolute;
    inset: 0;
    background:
      radial-gradient(ellipse 130px 200px at 230px 420px, var(--scene-red) 0%, rgba(200,38,43,0.85) 55%, rgba(200,38,43,0) 100%),
      radial-gradient(ellipse 90px 260px at 1150px 260px, var(--scene-red) 0%, rgba(200,38,43,0.8) 60%, rgba(200,38,43,0) 100%),
      radial-gradient(ellipse 70px 240px at 660px 300px, rgba(205,40,44,0.9) 0%, rgba(205,40,44,0) 100%),
      radial-gradient(ellipse 180px 220px at 880px 330px, var(--scene-light) 0%, rgba(233,230,228,0) 100%),
      radial-gradient(ellipse 130px 180px at 560px 200px, #f1efee 0%, rgba(241,239,238,0) 100%),
      radial-gradient(ellipse 160px 130px at 180px 170px, #d9d8d6 0%, rgba(217,216,214,0) 100%),
      linear-gradient(90deg, var(--scene-dark) 0%, #5a4a3a 20%, #8b6f68 38%, #c9b9b8 50%, #ddd6d4 70%, #6e5a55 90%, #a12a2c 100%);
    filter: blur(6px);
    transform: scale(1.04);
  }
  .hero-shade {
    position: absolute;
    inset: 0;
    background: rgba(0, 0, 0, 0.12);
  }
  .hero-content {
    position: absolute;
    inset: 0;
    text-align: center;
    color: var(--hero-white);
    text-shadow: 0 1px 3px rgba(0,0,0,0.25);
  }
  .hero-welcome {
    position: absolute;
    top: 98px;
    width: 100%;
    font-family: "Lora", Georgia, serif;
    font-weight: 700;
    font-size: 50px;
  }
  .hero-name {
    position: absolute;
    top: 180px;
    width: 100%;
    font-family: "Lora", Georgia, serif;
    font-weight: 700;
    font-size: 30px;
  }
  .hero-tagline {
    position: absolute;
    top: 277px;
    width: 100%;
    font-family: "Open Sans", Arial, sans-serif;
    font-size: 24px;
  }
  .hero-button {
    position: absolute;
    top: 354px;
    left: 518px;
    width: 161px;
    height: 41px;
    line-height: 41px;
    background: var(--accent);
    color: var(--hero-white);
    font-family: "Open Sans", Arial, sans-serif;
    font-size: 15px;
    text-transform: uppercase;
    text-decoration: none;
    text-shadow: none;
  }
  .social-links {
    position: absolute;
    top: 660px;
    left: 538px;
    display: flex;
    gap: 12px;
  }
  .social-links span {
    display: block;
    width: 20px;
    height: 20px;
    border-radius: 50%;
    background: var(--icon-grey);
  }
</style>
</head>
<body>
  <div class="page">
    <header class="site-header">
      <h1 class="site-title">TOWN PLATES IN MOTION</h1>
      <div class="nav-rule nav-rule--left"></div>
      <nav class="main-nav">
        <a class="is-active" href="#">Home</a>
        <a href="#">Join Us</a>
        <a href="#">Contact</a>
        <a href="#">About Us</a>
      </nav>
      <div class="nav-rule nav-rule--right"></div>
    </header>

    <section class="hero">
      <div class="hero-backdrop" role="img" aria-label="Blurred photo of a colourful red and white restaurant storefront"></div>
      <div class="hero-shade"></div>
      <div class="hero-content">
        <h2 class="hero-welcome">welcome</h2>
        <p class="hero-name">Town Plates In Motion</p>
        <p class="hero-tagline">Restaurant Specials, Menus and more.</p>
        <a class="hero-button" href="#">Lets Eat Local</a>
      </div>
    </section>

    <div class="social-links" aria-label="Social links">
      <span></span><span></span><span></span><span></span>
    </div>
  </div>
</body>
</html>
```